Banner Design Project

We are an Australian online lighting store based in Sydney.
Our website is "www.trelvamart.com.au"
We need someone you can create a 2 banners for our homepage.
We will have 3 banners rotating, the first banner will be our actual banner, the second one will be advertising Free Shipping Insurance and the third will advertising the 30 Day money back guaranty.
Don't be afraid to use words like Risk Free, 30 Day Money back Guaranty! etc....
The banner size:
599 x 186 px
The format should be given in .psd and .jpg
We need something slick and attractive that looks very promotional.
The banner should have the same look and feel as the website.
We are looking for someone long term, so if the job goes well, we might ask the person to design regularly for us in the future.

```html
<!DOCTYPE html>
<html lang="en">
<head>
<meta charset="UTF-8">
<title>30 Day Money Back Guarantee Banner</title>
<link href="https://fonts.googleapis.com/css2?family=Arimo:wght@700&display=swap" rel="stylesheet">
<style>
  :root {
    --bg-blue: #1637c9;
    --bg-mid: #3d5fd6;
    --bg-grey: #aab3c9;
    --bg-lavender: #c4c8e8;
    --burst-core: #fff45a;
    --burst-mid: #ffd400;
    --burst-edge: #ff9c00;
    --headline: #f7921e;
    --headline-shade: #c96a0a;
    --dollar-light: #7be37b;
    --dollar-dark: #0f8a2a;
    --lamp-light: #f4f4f6;
    --lamp-dark: #b9bcc4;
  }
  html, body {
    margin: 0;
    padding: 0;
    overflow: hidden;
    background: #ffffff;
  }
  .banner {
    position: relative;
    width: 1200px;
    height: 373px;
    overflow: hidden;
    background: linear-gradient(90deg, var(--bg-blue) 0%, var(--bg-mid) 35%, #7f8fc8 65%, var(--bg-grey) 88%, var(--bg-lavender) 100%);
  }
  .burst {
    position: absolute;
    inset: 0;
    width: 1200px;
    height: 373px;
  }
  .headline {
    position: absolute;
    left: 300px;
    top: 98px;
    width: 500px;
    margin: 0;
    text-align: center;
    font-family: "Arimo", Arial, sans-serif;
    font-weight: 700;
    font-size: 44px;
    line-height: 46px;
    letter-spacing: 0.5px;
    color: var(--headline);
    text-shadow: 2px 2px 0 var(--headline-shade);
    transform: rotate(-2deg);
  }
  .lamp {
    position: absolute;
    left: 368px;
    top: 192px;
    width: 344px;
    height: 98px;
    border-radius: 40px 50% 50% 40px / 50%;
    background: radial-gradient(ellipse at 55% 45%, var(--lamp-light) 0%, #dfe1e6 55%, var(--lamp-dark) 100%);
  }
  .dollar {
    position: absolute;
    top: 40px;
    width: 92px;
    height: 282px;
    border-radius: 40px;
    background: linear-gradient(90deg, var(--dollar-dark) 0%, var(--dollar-light) 50%, var(--dollar-dark) 100%);
  }
  .dollar--left { left: 0; }
  .dollar--right { left: 1106px; }
</style>
</head>
<body>
  <div class="banner">
    <svg class="burst" viewBox="0 0 1200 373" aria-hidden="true">
      <defs>
        <radialGradient id="burstFill" cx="50%" cy="50%" r="50%">
          <stop offset="0%" stop-color="var(--burst-core)"/>
          <stop offset="55%" stop-color="var(--burst-mid)"/>
          <stop offset="100%" stop-color="var(--burst-edge)"/>
        </radialGradient>
        <filter id="burstGlow" x="-20%" y="-20%" width="140%" height="140%">
          <feGaussianBlur stdDeviation="10"/>
        </filter>
        <polygon id="burstShape" points="100,0 77.3,10.2 96.6,25.9 72.1,29.9 86.6,50 61.9,47.5 70.7,70.7 47.5,61.9 50,86.6 29.9,72.1 25.9,96.6 10.2,77.3 0,100 -10.2,77.3 -25.9,96.6 -29.9,72.1 -50,86.6 -47.5,61.9 -70.7,70.7 -61.9,47.5 -86.6,50 -72.1,29.9 -96.6,25.9 -77.3,10.2 -100,0 -77.3,-10.2 -96.6,-25.9 -72.1,-29.9 -86.6,-50 -61.9,-47.5 -70.7,-70.7 -47.5,-61.9 -50,-86.6 -29.9,-72.1 -25.9,-96.6 -10.2,-77.3 0,-100 10.2,-77.3 25.9,-96.6 29.9,-72.1 50,-86.6 47.5,-61.9 70.7,-70.7 61.9,-47.5 86.6,-50 72.1,-29.9 96.6,-25.9 77.3,-10.2"/>
      </defs>
      <g transform="translate(620 182) scale(4.3 1.72)">
        <use href="#burstShape" fill="var(--burst-edge)" filter="url(#burstGlow)" opacity="0.9"/>
        <use href="#burstShape" fill="url(#burstFill)"/>
      </g>
    </svg>

    <h1 class="headline">30 DAY MONEY BACK<br>GUARANTEE</h1>

    <div class="lamp" role="img" aria-label="Photo of a metal halide lamp bulb lying horizontally"></div>

    <div class="dollar dollar--left" role="img" aria-label="Glossy green dollar sign"></div>
    <div class="dollar dollar--right" role="img" aria-label="Glossy green dollar sign"></div>
  </div>
</body>
</html>
```